B2B EDM Banner Design- Specialist Tech Company

We need a new top-of-email banner for our EDM campaigns for Varnel Brix (www.varnelbrix-example.com
). This banner will sit at the top of every email and must immediately signal the brand, look modern and professional, and be visually aligned with the tech/IT audience.
Size of the banner: Around 728x90 - it must fit at the top of an email blast.
Purpose of the Banner
Establish a strong, recognizable brand identity across all Varnel Brix EDMs
visually consistent with existing banners created for other brands (see reference examples provided)
Communicate Varnel Brix’s value proposition at a glance
Brand Name
Varnel Brix
Tagline (must appear in the banner)
“11,322 whitepapers from 726 companies”
Design Requirements
Style & Tone
Modern, clean, and professional
Tech-centric look and feel
High-quality, sleek, and corporate
Eye-catching but not cluttered
Should feel premium and authoritative
Layout & Composition
Full-width banner for email header
Horizontal orientation similar to the Plomtar and Quindle Staff Archive examples
Include space for the brand name/logo prominently on the left or centered
Integrate the tagline in a readable, secondary position
Optional: a subtle background texture or tech-related abstract pattern (circuitry, network nodes, gradient, etc.)
No busy imagery—should feel clean and trustworthy
Color Palette
Use colors consistent with Varnel Brix branding from www.varnelbrix-example.com
Blues, greys, blacks, and tech-style gradients preferred
Should feel consistent with a B2B IT audience
Typography
Clean, sans-serif fonts (professional/tech-aligned)
Brand name should be bold and prominent
Tagline should be smaller, but still readable on desktop and mobile
Imagery (if used)
Abstract tech shapes, network visuals, geometric patterns, or gradient overlays
Avoid photography of people
Keep imagery subtle so text remains legible
Call-to-Action Button (optional)
None required in this banner (unlike the HR examples)
Banner should remain a pure brand header
Deliverables
Final banner in PNG and JPG formats
2–3 design variations (if possible) for A/B testing
Dimensions optimized for EDM: ~600–700px wide (standard email width), proportionate height

```html
<!DOCTYPE html>
<html lang="en">
<head>
<meta charset="utf-8">
<title>Varnel Brix – EDM Header Banner</title>
<link rel="stylesheet" href="https://fonts.googleapis.com/css2?family=Montserrat:wght@400;700;800&display=swap">
<style>
  :root {
    --page-bg: #e8e6e7;
    --navy-deep: #07112a;
    --navy: #022a57;
    --royal: #0a3fd6;
    --electric: #1f6bff;
    --cyan: #3fe6f0;
    --brand-blue: #0fa0dc;
    --white: #ffffff;
  }
  * { margin: 0; padding: 0; box-sizing: border-box; }
  html, body {
    width: 1200px; height: 1200px; overflow: hidden;
    background: var(--page-bg);
    font-family: "Montserrat", sans-serif;
  }
  .banner {
    position: absolute; left: 88px; top: 324px;
    width: 1024px; height: 551px; overflow: hidden;
    background:
      radial-gradient(ellipse 520px 360px at 92% 40%, rgba(10,70,230,0.85), rgba(10,60,210,0) 70%),
      linear-gradient(180deg, var(--navy) 0%, #03204a 40%, var(--navy-deep) 100%);
    color: var(--white);
  }
  .particle-field {
    position: absolute; right: 0; bottom: 0; width: 620px; height: 320px;
    background:
      radial-gradient(ellipse 260px 90px at 88% 45%, rgba(63,230,240,0.45), rgba(63,230,240,0) 70%),
      radial-gradient(ellipse 420px 170px at 70% 60%, rgba(31,107,255,0.45), rgba(31,107,255,0) 70%);
  }
  .brand-mark {
    position: absolute; left: 36px; top: 48px;
    width: 140px; height: 140px; border-radius: 50%;
    background: var(--brand-blue);
  }
  .brand-name {
    position: absolute; left: 232px; top: 50px;
    font-weight: 800; font-size: 72px; line-height: 1;
    letter-spacing: 0.5px; text-transform: uppercase; white-space: nowrap;
    color: var(--white);
  }
  .brand-rule {
    position: absolute; left: 237px; top: 136px;
    width: 596px; height: 2px; background: var(--brand-blue);
  }
  .brand-tagline {
    position: absolute; left: 237px; top: 148px; width: 596px;
    display: flex; justify-content: space-between;
    font-weight: 700; font-size: 24px; line-height: 1.1;
  }
  .stat-number {
    position: absolute; left: 26px;
    font-weight: 800; font-size: 72px; line-height: 1;
    color: var(--brand-blue); letter-spacing: -1px;
  }
  .stat-label {
    position: absolute; left: 27px;
    font-weight: 400; font-size: 38px; line-height: 1;
    color: var(--white);
  }
  .stat-whitepapers { top: 280px; }
  .label-whitepapers { top: 352px; }
  .stat-companies { top: 403px; }
  .label-companies { top: 474px; }
</style>
</head>
<body>
  <section class="banner">
    <div class="particle-field" role="img" aria-label="Soft glowing blue and cyan bokeh particles drifting across the lower right"></div>

    <div class="brand-mark"></div>
    <h1 class="brand-name">Varnel Brix</h1>
    <div class="brand-rule"></div>
    <p class="brand-tagline">
      <span>F</span><span>O</span><span>R</span><span>&nbsp;</span><span>I</span><span>T</span><span>&nbsp;</span><span>P</span><span>R</span><span>O</span><span>F</span><span>E</span><span>S</span><span>S</span><span>I</span><span>O</span><span>N</span><span>A</span><span>L</span><span>S</span>
    </p>

    <p class="stat-number stat-whitepapers">11,322</p>
    <p class="stat-label label-whitepapers">whitepapers from</p>
    <p class="stat-number stat-companies">726</p>
    <p class="stat-label label-companies">companies</p>
  </section>
</body>
</html>
```